ALL TEXT Social Media Graphics

We are looking for a series of social media graphics for Instagram (new size: 4:5 (1080 x 1350 pixels) ratio that are ALL TEXT. We want the following quotes below on each graphic; one quote per graphic. AND, In very small letters at the bottom of each graphic, add @KPBrandellLive
The look and feel of these graphics should be complimentary to the color palette attached below; but keep them simple. But the design is up to you; at the end of this document, I provided various samples of all text graphics that I like as examples.
The Quotes are in the attached WORD document
Target Market(s)
women trying to lose weight
Look and feel
Each slider illustrates characteristics of the customer's brand and the style your logo design should communicate.

```html
<!DOCTYPE html>
<html lang="en">
<head>
<meta charset="utf-8">
<title>Sun Glow Summer Slimdown – Social Graphics</title>
<link href="https://fonts.googleapis.com/css2?family=Bebas+Neue&family=Outfit:wght@400;500&display=swap" rel="stylesheet">
<style>
  :root{
    --backdrop:#a3a3a3;
    --card:#ffffff;
    --berry:#b3124f;
    --ink:#111111;
  }
  *{margin:0;padding:0;box-sizing:border-box}
  html,body{width:1200px;height:3132px;overflow:hidden;background:var(--backdrop)}
  .board{position:relative;width:1200px;height:3132px}
  .post{
    position:absolute;width:456px;height:569px;background:var(--card);
    display:flex;flex-direction:column;justify-content:center;
    padding:0 63px 80px 39px;
  }
  .col-l{left:128px}.col-r{left:601px}
  .row-1{top:102px}.row-2{top:688px}.row-3{top:1274px}.row-4{top:1860px}.row-5{top:2446px}
  .headline,.cta{
    font-family:"Bebas Neue","Oswald",sans-serif;color:var(--berry);
    line-height:.9;white-space:nowrap;
  }
  .headline span,.cta span,.body span{display:block;font-size:var(--fs)}
  .body{
    font-family:"Outfit",sans-serif;font-weight:500;color:var(--ink);
    line-height:1.05;white-space:nowrap;margin:14px 0 16px;letter-spacing:-.2px;
  }
  .keyword{display:inline!important;color:var(--ink);font-style:italic}
  .handle{
    position:absolute;right:63px;bottom:40px;
    font-family:"Outfit",sans-serif;font-weight:500;font-size:13px;color:var(--ink);
  }
</style>
</head>
<body>
<main class="board">

  <section class="post col-l row-1">
    <h2 class="headline"><span style="--fs:50px">You can absolutely</span><span style="--fs:45px">be down 20–30 pounds</span><span style="--fs:53px">by end of summer.</span></h2>
    <p class="body"><span style="--fs:30px">All it takes is the right</span><span style="--fs:26px">plan—and you’ve found it.</span></p>
    <p class="cta"><span style="--fs:50px">Comment <em class="keyword">“Sun Glow”</em></span><span style="--fs:56px">for the Sun Glow</span><span style="--fs:56px">summer slimdown!</span></p>
    <p class="handle">@KPBrandellLive</p>
  </section>

  <section class="post col-r row-1">
    <h2 class="headline"><span style="--fs:65px">You don’t need</span><span style="--fs:43px">another diet—you need</span><span style="--fs:45px">a system that works.</span></h2>
    <p class="body"><span style="--fs:34px">Drop 30 pounds with</span><span style="--fs:21px">the Sun Glow Summer Slimdown.</span></p>
    <p class="cta"><span style="--fs:52px">Comment <em class="keyword">“Summer”</em></span><span style="--fs:70px">to start now.</span></p>
    <p class="handle">@KPBrandellLive</p>
  </section>

  <section class="post col-l row-2">
    <h2 class="headline"><span style="--fs:41px">This summer ain’t over</span><span style="--fs:60px">and neither are</span><span style="--fs:57px">your body goals.</span></h2>
    <p class="body"><span style="--fs:34px">Drop 30 pounds with</span><span style="--fs:21px">the Sun Glow Summer Slimdown.</span></p>
    <p class="cta"><span style="--fs:50px">Comment <em class="keyword">“Sun Glow”</em></span><span style="--fs:60px">to get the plan</span></p>
    <p class="handle">@KPBrandellLive</p>
  </section>

  <section class="post col-r row-2">
    <h2 class="headline"><span style="--fs:62px">If your goal is</span><span style="--fs:37px">a tiny waist, flat belly,</span></h2>
    <p class="body"><span style="--fs:33px">And 30 pounds down</span><span style="--fs:43px">this is the plan.</span></p>
    <p class="cta"><span style="--fs:52px">Comment <em class="keyword">“Summer”</em></span><span style="--fs:48px">to join the Sun Glow</span><span style="--fs:50px">summer slimdown!</span></p>
    <p class="handle">@KPBrandellLive</p>
  </section>

  <section class="post col-l row-3">
    <h2 class="headline"><span style="--fs:50px">There’s still time</span><span style="--fs:43px">to drop the 30 pounds</span><span style="--fs:43px">and slay this summer.</span></h2>
    <p class="body"><span style="--fs:33px">The Sun Glow Summer</span><span style="--fs:24px">Slimdown has the blueprint.</span></p>
    <p class="cta"><span style="--fs:50px">Comment <em class="keyword">“Sun Glow” !</em></span></p>
    <p class="handle">@KPBrandellLive</p>
  </section>

  <section class="post col-r row-3">
    <h2 class="headline"><span style="--fs:60px">Snatched waist,</span><span style="--fs:82px">flat tummy,</span><span style="--fs:53px">30 pounds lighter</span></h2>
    <p class="body"><span style="--fs:28px">That’s what the Sun Glow</span><span style="--fs:38px">Summer Slimdown</span><span style="--fs:36px">Challenge delivers.</span></p>
    <p class="cta"><span style="--fs:50px">Comment <em class="keyword">“Sun Glow” !</em></span><span style="--fs:60px">to get the plan</span></p>
    <p class="handle">@KPBrandellLive</p>
  </section>

  <section class="post col-l row-4">
    <h2 class="headline"><span style="--fs:45px">Nothing feels better</span><span style="--fs:34px">than seeing that scale drop</span><span style="--fs:57px">week after week.</span></h2>
    <p class="body"><span style="--fs:28px">Let’s lose up to 30 pounds</span><span style="--fs:30px">this summer—together.</span></p>
    <p class="cta"><span style="--fs:52px">Comment <em class="keyword">“Summer”</em></span><span style="--fs:48px">to join the Sun Glow</span><span style="--fs:50px">summer slimdown!</span></p>
    <p class="handle">@KPBrandellLive</p>
  </section>

  <section class="post col-r row-4">
    <h2 class="headline"><span style="--fs:48px">Sis, we’re dropping</span><span style="--fs:31px">belly flat and saying goodbye</span><span style="--fs:48px">to stubborn pounds.</span></h2>
    <p class="body"><span style="--fs:42px">Join the Sun Glow</span><span style="--fs:38px">Summer Slimdown</span></p>
    <p class="cta"><span style="--fs:52px">Comment <em class="keyword">“Summer”</em></span></p>
    <p class="handle">@KPBrandellLive</p>
  </section>

  <section class="post col-l row-5">
    <h2 class="headline"><span style="--fs:72px">Don’t wait ‘til</span><span style="--fs:82px">next summer</span><span style="--fs:72px">to get right.</span></h2>
    <p class="body"><span style="--fs:40px">The time is NOW.</span><span style="--fs:35px">Drop 30 pounds with</span><span style="--fs:21px">the Sun Glow Summer Slimdown.</span></p>
    <p class="cta"><span style="--fs:52px">Comment <em class="keyword">“Summer”</em></span></p>
    <p class="handle">@KPBrandellLive</p>
  </section>

  <section class="post col-r row-5">
    <h2 class="headline"><span style="--fs:50px">You’ve got 8 weeks</span><span style="--fs:45px">and the perfect plan</span><span style="--fs:50px">to drop 30 pounds.</span></h2>
    <p class="body"><span style="--fs:39px">Let’s get snatched</span><span style="--fs:40px">this summer with</span><span style="--fs:21px">the Sun Glow Summer Slimdown.</span></p>
    <p class="cta"><span style="--fs:52px">Comment <em class="keyword">“Summer”</em></span></p>
    <p class="handle">@KPBrandellLive</p>
  </section>

</main>
</body>
</html>
```